Website update for Harbor Broker Ledger & Payroll Services

Our website needs updating
www.harborbrokerledgers.com
Here are some of our latest print pieces to use as a guide?
I have also attached our graphic identity guide which includes the Pantone colors

Target Market(s)

Insurance Agencies

Industry/Entity Type

Accounting

Number of Pages Required

5+ page

```html
<!DOCTYPE html>
<html lang="en">
<head>
<meta charset="utf-8">
<title>Harbor Broker Ledger & Payroll Services</title>
<link href="https://fonts.googleapis.com/css2?family=Open+Sans:wght@300;400;600;700&display=swap" rel="stylesheet">
<style>
:root{
  --teal:#2bb5ad;
  --teal-dark:#1f8f89;
  --ink:#333;
  --muted:#777;
  --dark:#2a2a2a;
  --darker:#1c1c1c;
  --panel:#323232;
  --light:#f4f4f4;
  --white:#fff;
}
*{margin:0;padding:0;box-sizing:border-box}
html,body{width:1200px;height:2548px;overflow:hidden}
body{font-family:"Open Sans",Arial,sans-serif;color:var(--ink);background:var(--white);position:relative}
.abs{position:absolute}

/* header */
.site-header{position:absolute;left:0;top:0;width:1200px;height:72px;background:rgba(30,30,30,.55);z-index:2}
.brand{position:absolute;left:90px;top:14px;display:flex;align-items:center;gap:10px}
.brand-mark{width:40px;height:40px;background:var(--teal)}
.brand-name{color:var(--white);font-weight:700;font-size:26px;letter-spacing:1px}
.main-nav{position:absolute;right:90px;top:28px;display:flex;gap:26px}
.main-nav a{color:var(--white);font-size:13px;font-weight:600;text-decoration:none;letter-spacing:.5px}
.main-nav a.active{color:var(--teal)}

/* hero */
.hero{position:absolute;left:0;top:0;width:1200px;height:640px;background:linear-gradient(160deg,#dfe4e6 0%,#c9cfd2 45%,#a7adb0 100%)}
.hero-band{position:absolute;left:0;top:510px;width:1200px;height:110px;background:linear-gradient(90deg,rgba(30,30,30,.45),rgba(30,30,30,.15))}
.hero-title{position:absolute;left:150px;top:520px;color:var(--white);font-size:32px;font-weight:600;line-height:44px}
.hero-title span{font-weight:300;display:block;padding-left:110px}

/* intro */
.intro{position:absolute;left:0;top:640px;width:1200px;height:410px;background:var(--white)}
.chart{position:absolute;left:200px;top:60px}
.intro-heading{position:absolute;left:640px;top:56px;width:440px;color:var(--teal);font-size:22px;font-weight:600;line-height:30px}
.intro-item{position:absolute;left:640px;width:440px;display:flex;gap:20px;align-items:flex-start}
.intro-item p{font-size:12px;line-height:18px;color:var(--muted)}

/* services */
.services{position:absolute;left:0;top:1050px;width:1200px;height:450px;background:linear-gradient(180deg,#3c3c3c,#262626)}
.section-title{position:absolute;width:1200px;text-align:center;color:var(--teal);font-size:26px;font-weight:600;letter-spacing:1px}
.service{position:absolute;width:220px;text-align:center;top:120px}
.service-icon{width:118px;height:118px;margin:0 auto;border-radius:50%;background:var(--white);border:4px solid var(--teal);display:flex;align-items:center;justify-content:center}
.service h3{margin-top:24px;color:var(--white);font-size:14px;font-weight:600;line-height:20px}
.arrow{position:absolute}

/* how it works */
.how-photo{position:absolute;left:0;top:1500px;width:640px;height:380px;background:linear-gradient(135deg,#e9eef2,#9fb1c3 60%,#2f4663)}
.how-panel{position:absolute;left:640px;top:1500px;width:560px;height:380px;background:var(--panel)}
.how-panel h2{position:absolute;left:90px;top:42px;color:var(--white);font-size:26px;font-weight:600;letter-spacing:1px}
.how-list{position:absolute;left:90px;top:110px;width:390px;list-style:none}
.how-list li{position:relative;padding-left:24px;margin-bottom:18px;color:#ccc;font-size:12px;line-height:18px}
.how-list li::before{content:"";position:absolute;left:0;top:5px;width:8px;height:8px;background:var(--teal);border-radius:50%}
.btn-outline{position:absolute;left:175px;top:290px;width:120px;height:38px;border:2px solid var(--teal);color:var(--teal);font-size:13px;font-weight:600;text-align:center;line-height:34px;border-radius:3px}

/* team */
.team{position:absolute;left:0;top:1880px;width:1200px;height:340px;background:var(--white)}
.member{position:absolute;top:100px;width:150px;text-align:center}
.member-photo{width:104px;height:104px;margin:0 auto;border-radius:50%;border:3px solid var(--teal);background:linear-gradient(160deg,#e8d4c4,#8a6a57)}
.member h4{margin-top:12px;font-size:12px;font-weight:600;color:var(--ink)}
.member p{font-size:11px;color:var(--muted);line-height:15px}

/* footer */
.site-footer{position:absolute;left:0;top:2220px;width:1200px;height:280px;background:var(--dark)}
.footer-brand{position:absolute;left:0;top:26px;width:1200px;display:flex;justify-content:center;align-items:center;gap:10px}
.footer-brand .brand-mark{width:34px;height:34px}
.footer-brand .brand-name{font-size:24px}
.subscribe-title{position:absolute;left:0;top:86px;width:1200px;text-align:center;color:var(--white);font-size:14px;font-weight:600}
.subscribe-form{position:absolute;left:450px;top:118px;display:flex}
.subscribe-input{width:210px;height:32px;background:#444;border:1px solid #555;color:#999;font-size:12px;line-height:30px;padding-left:10px}
.subscribe-btn{width:80px;height:32px;background:var(--teal);color:var(--white);font-size:11px;font-weight:700;text-align:center;line-height:32px}
.contact-block{position:absolute;left:100px;top:178px;color:#bbb;font-size:12px;line-height:20px}
.address-block{position:absolute;right:100px;top:178px;color:#bbb;font-size:12px;line-height:20px;text-align:left}
.bottom-bar{position:absolute;left:0;top:2500px;width:1200px;height:48px;background:var(--darker)}
.social{position:absolute;left:100px;top:14px;display:flex;gap:8px}
.social span{width:20px;height:20px;background:var(--teal)}
.copyright{position:absolute;right:100px;top:16px;color:#888;font-size:11px}
</style>
</head>
<body>

<section class="hero" role="img" aria-label="Photo of three smiling office colleagues reviewing work together at a desk"></section>
<div class="hero-band"></div>
<h1 class="hero-title">Specialists in providing accounting support services<span>to Independent Insurance Agencies</span></h1>

<header class="site-header">
  <div class="brand"><div class="brand-mark"></div><div class="brand-name">HBLP</div></div>
  <nav class="main-nav">
    <a class="active" href="#">HOME</a><a href="#">ABOUT</a><a href="#">COMPANY</a><a href="#">SERVICES</a><a href="#">HOW IT WORKS</a><a href="#">RESOURCES</a><a href="#">CONTACT US</a><a href="#">BLOG</a>
  </nav>
</header>

<section class="intro">
  <svg class="chart" width="250" height="170" viewBox="0 0 250 170">
    <rect x="1" y="1" width="248" height="168" fill="#fff" stroke="#bbb"/>
    <text x="125" y="16" font-family="Open Sans, sans-serif" font-size="8" text-anchor="middle" fill="#333">Agency revenue and expenses by quarter</text>
    <line x1="20" y1="135" x2="235" y2="135" stroke="#999"/>
    <g fill="#2d6fb3">
      <rect x="26" y="110" width="9" height="25"/><rect x="42" y="104" width="9" height="31"/><rect x="58" y="100" width="9" height="35"/><rect x="74" y="96" width="9" height="39"/>
      <rect x="90" y="92" width="9" height="43"/><rect x="106" y="86" width="9" height="49"/><rect x="122" y="80" width="9" height="55"/><rect x="138" y="74" width="9" height="61"/>
      <rect x="154" y="66" width="9" height="69"/><rect x="170" y="58" width="9" height="77"/><rect x="186" y="48" width="9" height="87"/><rect x="202" y="38" width="9" height="97"/><rect x="218" y="30" width="9" height="105"/>
    </g>
    <polyline points="30,118 46,114 62,112 78,108 94,104 110,100 126,96 142,90 158,84 174,76 190,68 206,60 222,50" fill="none" stroke="#2bb5ad" stroke-width="2"/>
    <rect x="70" y="148" width="8" height="6" fill="#2d6fb3"/><text x="82" y="154" font-size="7" fill="#555" font-family="Open Sans, sans-serif">Revenue</text>
    <rect x="130" y="150" width="10" height="2" fill="#2bb5ad"/><text x="144" y="154" font-size="7" fill="#555" font-family="Open Sans, sans-serif">Expenses</text>
  </svg>
  <h2 class="intro-heading">Need help with your insurance agency's accounting and bookkeeping?</h2>
  <div class="intro-item" style="top:150px">
    <svg width="34" height="26" viewBox="0 0 34 26"><circle cx="10" cy="8" r="5" fill="#888"/><circle cx="24" cy="8" r="5" fill="#888"/><rect x="3" y="15" width="14" height="10" rx="3" fill="#888"/><rect x="17" y="15" width="14" height="10" rx="3" fill="#888"/></svg>
    <p>Let our team of trained agency bookkeepers handle the daily ledger work for you.</p>
  </div>
  <div class="intro-item" style="top:220px">
    <svg width="34" height="26" viewBox="0 0 34 26"><rect x="2" y="2" width="30" height="18" rx="2" fill="none" stroke="#888" stroke-width="2"/><rect x="12" y="21" width="10" height="4" fill="#888"/></svg>
    <p>Access to a secure reporting portal that keeps your agency numbers current every day.</p>
  </div>
  <div class="intro-item" style="top:290px">
    <svg width="34" height="26" viewBox="0 0 34 26"><circle cx="12" cy="13" r="10" fill="none" stroke="#888" stroke-width="2"/><text x="12" y="18" font-size="12" text-anchor="middle" fill="#888" font-family="Open Sans, sans-serif">$</text><rect x="24" y="6" width="8" height="14" fill="#888"/></svg>
    <p>Be connected with certified financial professionals who understand how independent agencies operate.</p>
  </div>
</section>

<section class="services" role="img" aria-label="Dimmed photo of a business team in a meeting as section background">
  <h2 class="section-title" style="top:58px">OUR SERVICES</h2>
  <svg class="arrow" style="left:120px;top:166px" width="20" height="30" viewBox="0 0 20 30"><polyline points="16,3 4,15 16,27" fill="none" stroke="#fff" stroke-width="4"/></svg>
  <svg class="arrow" style="left:1060px;top:166px" width="20" height="30" viewBox="0 0 20 30"><polyline points="4,3 16,15 4,27" fill="none" stroke="#fff" stroke-width="4"/></svg>
  <div class="service" style="left:190px">
    <div class="service-icon"><svg width="54" height="42" viewBox="0 0 54 42"><ellipse cx="26" cy="22" rx="22" ry="16" fill="#e88aa8"/><rect x="14" y="34" width="6" height="8" fill="#e88aa8"/><rect x="32" y="34" width="6" height="8" fill="#e88aa8"/><rect x="20" y="4" width="10" height="3" fill="#555"/></svg></div>
    <h3>Record Direct Bill<br>Commissions</h3>
  </div>
  <div class="service" style="left:490px">
    <div class="service-icon"><svg width="56" height="36" viewBox="0 0 56 36"><rect x="2" y="4" width="52" height="28" fill="#7cc36a" stroke="#4a8f3c" stroke-width="2"/><circle cx="28" cy="18" r="8" fill="none" stroke="#4a8f3c" stroke-width="2"/></svg></div>
    <h3>Reconcile &amp; Pay Agency<br>Bill Premiums</h3>
  </div>
  <div class="service" style="left:790px">
    <div class="service-icon"><svg width="56" height="40" viewBox="0 0 56 40"><rect x="4" y="8" width="48" height="24" fill="none" stroke="#d33" stroke-width="3"/><rect x="10" y="17" width="36" height="6" fill="#d33"/></svg></div>
    <h3>Reconcile Customer Account<br>Receivable</h3>
  </div>
</section>

<div class="how-photo" role="img" aria-label="Photo of a businessman in a suit writing at a desk beside a computer"></div>
<section class="how-panel">
  <h2>HOW IT WORKS</h2>
  <ul class="how-list">
    <li>HBLP has the expertise to perform all of your bookkeeping functions on or from your office using remote access.</li>
    <li>Agent information, licence and client data is collected and entered securely.</li>
    <li>We review your monthly accounts and report back to you the same day.</li>
  </ul>
  <div class="btn-outline">Read More</div>
</section>

<section class="team">
  <h2 class="section-title" style="top:36px">TEAM MEMBERS</h2>
  <svg class="arrow" style="left:160px;top:140px" width="14" height="22" viewBox="0 0 14 22"><polyline points="11,2 3,11 11,20" fill="none" stroke="#bbb" stroke-width="3"/></svg>
  <svg class="arrow" style="left:1026px;top:140px" width="14" height="22" viewBox="0 0 14 22"><polyline points="3,2 11,11 3,20" fill="none" stroke="#bbb" stroke-width="3"/></svg>
  <div class="member" style="left:185px"><div class="member-photo" role="img" aria-label="Portrait photo of team member"></div><h4>Mara Lindqvist</h4><p>Accounting Specialist</p></div>
  <div class="member" style="left:345px"><div class="member-photo" role="img" aria-label="Portrait photo of team member"></div><h4>Tessa Rowe</h4><p>Accounting Assistant</p></div>
  <div class="member" style="left:513px"><div class="member-photo" role="img" aria-label="Portrait photo of team member"></div><h4>Joan Whitcombe</h4><p>Principal</p></div>
  <div class="member" style="left:685px"><div class="member-photo" role="img" aria-label="Portrait photo of team member"></div><h4>Owen Pratley</h4><p>Financial Analyst for<br>Affiliate Agencies</p></div>
  <div class="member" style="left:853px"><div class="member-photo" role="img" aria-label="Portrait photo of team member"></div><h4>Ruth Ellery</h4><p>Bank Reconciliation Specialist</p></div>
</section>

<footer class="site-footer">
  <div class="footer-brand"><div class="brand-mark"></div><div class="brand-name">HBLP</div></div>
  <div class="subscribe-title">Subscribe to our Newsletter</div>
  <div class="subscribe-form"><div class="subscribe-input">Your email</div><div class="subscribe-btn">SIGN UP</div></div>
  <div class="contact-block">Phone: (555) 014-2290<br>Fax: (555) 014-2291<br>Email: hello@harborbrokerledgers.com</div>
  <div class="address-block">Harbor Broker Ledger &amp; Payroll Services<br>48 Lighthouse Road<br>Harborview, CT 06000</div>
</footer>
<div class="bottom-bar">
  <div class="social"><span></span><span></span><span></span><span></span></div>
  <div class="copyright">Copyright © 2016 Harbor Broker Ledger &amp; Payroll Services. All rights reserved.</div>
</div>

</body>
</html>
```